Graphic for Bad Ass Music Business Course
The Best Music Business Course on the Web
Creative Brief
We've launched an online interactive set of videos to teach the music business. It is for aspiring musicians and business professionals that want to learn about the real music business. The product is over 150 videos, transcriptions, quiz questions, and accompanying supplemental video materials. The host/ star of the series was the manager for the rock and roll band GLASSMOTH for 17 years and is a long time executive of the record business. Currently, he is the host of our internet talk show "Tolvar LIVE" where we've had over 100 videos with the most successful people in the music business both artists and professionals. The show is where entertainment, education, mentoring, and the entertainment business collide. We need an official graphic for our course that we can post around social media, post to our website, and embody the attitude, message and spirit of our course. For inspiration, check out our website for the course: www.tolvaracademy-example.com The graphic should communicate that this is "not your typical course". Why is that? Because we take a specific approach to teaching the music business by learning from people who have been there and done that. Going out and trying to make something happen and learning from experienced people in the business is the best way to learn the music business. Imagine being someone who is serious about making a career in the music business seeing this graphic. Or the parent of an aspiring musician. It should inspire you to want to sign up. It should tell you that "wow, this guy really looks like he knows what he's talking about I want to learn more about this course." As you can kind of tell in this creative brief, we work in a fun, loose atmosphere but we always strive to maintain a quality, professional edge. I encourage you to take that same style and try to put it in the graphic! Think: Cold Harbor, the velvet anchors, and Rock and Roll. Title of the Course: Backstage Playbook for the Modern Sound Trade Subtitle: The real music business from a real music business professional somewhere on the page write: with Mark "Tolvar" Dunsby
Entertainment
Aspiring rock stars, aspiring managers of rock bands, people dreaming of doing something big in the music business, guitarists, DJs, Producers... It's a combination of creative people and business people with an entertainment, show-business flare.

```html
<!DOCTYPE html>
<html lang="en">
<head>
<meta charset="utf-8">
<title>The Best Music Business Course on the Web</title>
<link rel="stylesheet" href="https://fonts.googleapis.com/css2?family=Raleway:ital,wght@0,300;0,400;0,800;1,300;1,400&display=swap">
<style>
  :root {
    --sky-deep: #0f6fae;
    --sky-mid: #1f8fd0;
    --sky-light: #5cc2ee;
    --portrait-warm: #f0a24a;
    --portrait-pink: #e2507a;
    --portrait-violet: #6a3fb0;
    --ink-white: #ffffff;
  }
  html, body {
    margin: 0;
    padding: 0;
    width: 1200px;
    height: 588px;
    overflow: hidden;
    background: var(--sky-mid);
  }
  .banner {
    position: relative;
    width: 1200px;
    height: 588px;
    overflow: hidden;
    background:
      radial-gradient(ellipse 70% 90% at 75% 35%, var(--sky-light) 0%, var(--sky-mid) 45%, var(--sky-deep) 100%);
    font-family: "Raleway", sans-serif;
    color: var(--ink-white);
  }
  .host-portrait {
    position: absolute;
    left: 560px;
    top: 0;
    width: 640px;
    height: 588px;
  }
  .course-title {
    position: absolute;
    left: 14px;
    top: 336px;
    margin: 0;
    font-size: 17px;
    font-weight: 400;
    font-style: italic;
    letter-spacing: 0.5px;
    line-height: 1;
  }
  .headline {
    position: absolute;
    left: 12px;
    top: 368px;
    margin: 0;
    text-transform: uppercase;
    line-height: 1;
  }
  .headline-lead,
  .headline-tail {
    display: block;
    font-weight: 300;
    font-size: 40px;
    line-height: 44px;
    letter-spacing: 0.5px;
  }
  .headline-main {
    display: block;
    font-weight: 800;
    font-size: 43px;
    line-height: 48px;
    letter-spacing: 0.3px;
  }
  .headline-tail em {
    font-style: italic;
    font-weight: 300;
  }
  .subtitle {
    position: absolute;
    left: 12px;
    top: 526px;
    margin: 0;
    font-size: 21px;
    line-height: 1;
    font-weight: 400;
    letter-spacing: 0.4px;
    text-transform: uppercase;
  }
  .subtitle strong {
    font-weight: 800;
  }
  .subtitle em {
    font-style: italic;
    font-weight: 300;
  }
  .host-credit {
    position: absolute;
    right: 10px;
    bottom: 8px;
    margin: 0;
    font-size: 11px;
    font-weight: 400;
    letter-spacing: 0.5px;
    text-transform: uppercase;
  }
</style>
</head>
<body>
  <main class="banner">
    <svg class="host-portrait" viewBox="0 0 640 588" role="img" aria-label="Colourful pop-art portrait of the course host, smiling broadly in dark glasses">
      <defs>
        <linearGradient id="portraitTone" x1="0" y1="0" x2="1" y2="1">
          <stop offset="0" stop-color="var(--portrait-warm)"/>
          <stop offset="0.55" stop-color="var(--portrait-pink)"/>
          <stop offset="1" stop-color="var(--portrait-violet)"/>
        </linearGradient>
      </defs>
      <path d="M40 588 C60 470 70 360 110 250 C150 120 250 30 390 10 C500 0 600 40 640 90 L640 588 Z" fill="url(#portraitTone)"/>
    </svg>

    <p class="course-title">Backstage Playbook for the Modern Sound Trade</p>

    <h1 class="headline">
      <span class="headline-lead">The Best</span>
      <span class="headline-main">Music Business Course</span>
      <span class="headline-tail">On the <em>Web</em></span>
    </h1>

    <p class="subtitle">The <em>Real</em> <strong>Music Business</strong> from <em>a Real</em> <strong>Music Business Professional</strong></p>

    <p class="host-credit">with Mark "Tolvar" Dunsby</p>
  </main>
</body>
</html>
```